Stationery For Upscale Concierge Company

Create stationary that looks good in black and white and uses the attached logo. Needs to be upscale using upscale fonts and layout. Use the attached logo. Reverse out if necessary.

```html
<!DOCTYPE html>
<html lang="en">
<head>
<meta charset="utf-8">
<title>North Harbor Stationery</title>
<link href="https://fonts.googleapis.com/css2?family=Arimo:wght@400;700&display=swap" rel="stylesheet">
<style>
  :root {
    --backdrop: #d6d6d6;
    --paper: #f7f7f7;
    --ink: #262626;
    --ink-deep: #1c1c1c;
    --on-dark: #f2f2f2;
    --muted: #3a3a3a;
  }
  * { margin: 0; padding: 0; box-sizing: border-box; }
  html, body { width: 1200px; height: 991px; overflow: hidden; }
  body {
    background: var(--backdrop);
    font-family: "Arimo", Arial, sans-serif;
    color: var(--ink);
    position: relative;
  }
  .piece { position: absolute; overflow: hidden; }
  .paper { background: var(--paper); }
  .dark { background: var(--ink); color: var(--on-dark); }

  .wordmark {
    font-family: "Arimo", Arial, sans-serif;
    font-weight: 400;
    text-transform: uppercase;
    letter-spacing: 0.12em;
    white-space: nowrap;
    display: flex;
    align-items: center;
    gap: 0.5em;
    position: absolute;
    transform: translateX(-50%);
  }
  .wordmark .mark-square {
    width: 0.7em; height: 0.7em;
    background: currentColor;
    display: inline-block;
  }

  .bottom-swoop { position: absolute; left: 0; bottom: 0; width: 100%; }

  /* Letterhead */
  .letterhead { left: 71px; top: 103px; width: 399px; height: 561px; }
  .letterhead .wordmark { left: 200px; top: 58px; font-size: 13px; }
  .contact-row {
    position: absolute; left: 0; top: 505px; width: 100%;
    display: flex; justify-content: space-around;
    font-size: 6px; line-height: 1.35; text-align: center; color: var(--muted);
  }
  .contact-item { display: flex; flex-direction: column; align-items: center; gap: 5px; }
  .contact-item svg { width: 12px; height: 12px; }
  .contact-divider { position: absolute; left: 190px; top: 506px; width: 1px; height: 36px; background: #bbb; }

  /* Folder */
  .folder { left: 507px; top: 90px; width: 433px; height: 574px; border-radius: 4px; }
  .folder .spine { position: absolute; left: 0; top: 0; width: 27px; height: 100%; background: var(--ink-deep); }
  .folder .wordmark { left: 217px; top: 112px; font-size: 20px; color: var(--on-dark); }
  .folder .site { position: absolute; left: 0; width: 100%; top: 528px; text-align: center; font-size: 7px; }

  .site b { font-weight: 700; }

  /* Business cards */
  .card-front { left: 66px; top: 696px; width: 170px; height: 93px; }
  .card-front .wordmark { left: 48px; top: 38px; font-size: 8px; letter-spacing: 0.08em; }
  .card-front .rule { position: absolute; left: 89px; top: 26px; width: 1px; height: 42px; background: #999; }
  .card-details { position: absolute; left: 95px; top: 27px; font-size: 3.6px; line-height: 1.45; color: var(--muted); }
  .card-details .name { font-size: 5px; font-weight: 700; color: var(--ink); margin-bottom: 2px; }
  .card-details .gap { height: 3px; }

  .card-back { left: 66px; top: 810px; width: 170px; height: 93px; }
  .card-back .wordmark { left: 85px; top: 36px; font-size: 9px; color: var(--on-dark); }
  .card-back .site { position: absolute; left: 0; width: 100%; top: 77px; text-align: center; font-size: 4px; }

  /* Envelope front */
  .envelope-front { left: 266px; top: 696px; width: 415px; height: 208px; }
  .envelope-front .wordmark { left: 72px; top: 36px; font-size: 11px; transform: none; }
  .return-address { position: absolute; left: 22px; top: 175px; display: flex; gap: 6px; align-items: center; font-size: 6px; line-height: 1.3; color: var(--muted); }
  .return-address svg { width: 11px; height: 11px; }

  /* Envelope back */
  .envelope-back { left: 718px; top: 696px; width: 415px; height: 208px; }
  .envelope-back .flap { position: absolute; left: 0; top: 0; width: 100%; height: 59px; }
  .envelope-back .mark-square-lg {
    position: absolute; left: 203px; top: 22px; width: 10px; height: 10px; background: var(--on-dark);
  }
  .envelope-back .site { position: absolute; left: 0; width: 100%; top: 178px; text-align: center; font-size: 5px; }
</style>
</head>
<body>

<!-- Letterhead -->
<section class="piece paper letterhead">
  <div class="wordmark"><span class="mark-square"></span>North Harbor</div>
  <div class="contact-divider"></div>
  <div class="contact-row">
    <div class="contact-item">
      <svg viewBox="0 0 24 24"><path d="M12 2a7 7 0 0 0-7 7c0 5 7 13 7 13s7-8 7-13a7 7 0 0 0-7-7zm0 9.5A2.5 2.5 0 1 1 12 6.5a2.5 2.5 0 0 1 0 5z" fill="#262626"/></svg>
      <span>218 Laurel Ave, #4<br>Oakland, CA 94610</span>
    </div>
    <div class="contact-item">
      <svg viewBox="0 0 24 24"><path d="M6.6 10.8a15 15 0 0 0 6.6 6.6l2.2-2.2a1 1 0 0 1 1-.25 11.4 11.4 0 0 0 3.6.57 1 1 0 0 1 1 1V20a1 1 0 0 1-1 1A17 17 0 0 1 3 4a1 1 0 0 1 1-1h3.5a1 1 0 0 1 1 1c0 1.25.2 2.45.57 3.57a1 1 0 0 1-.25 1z" fill="#262626"/></svg>
      <span>415-555-0142</span>
    </div>
    <div class="contact-item">
      <svg viewBox="0 0 24 24"><path d="M3 5h18v14H3z" fill="#262626"/><path d="M3 5l9 7 9-7" fill="none" stroke="#f7f7f7" stroke-width="1.6"/></svg>
      <span>info@northharbor.com</span>
    </div>
    <div class="contact-item">
      <svg viewBox="0 0 24 24" fill="none" stroke="#262626" stroke-width="1.5"><circle cx="12" cy="12" r="9"/><ellipse cx="12" cy="12" rx="4" ry="9"/><path d="M3 12h18M5 7h14M5 17h14"/></svg>
      <span>www.northharbor.us</span>
    </div>
  </div>
  <svg class="bottom-swoop" viewBox="0 0 399 10" height="10" preserveAspectRatio="none"><path d="M0 10 Q200 -6 399 10 Z" fill="#262626"/></svg>
</section>

<!-- Presentation folder -->
<section class="piece dark folder">
  <div class="spine"></div>
  <div class="wordmark"><span class="mark-square"></span>North Harbor</div>
  <div class="site">www.<b>northharbor</b>.us</div>
</section>

<!-- Business card, front -->
<section class="piece paper card-front">
  <div class="wordmark"><span class="mark-square"></span>North Harbor</div>
  <div class="rule"></div>
  <div class="card-details">
    <div class="name">ELENA MARSH</div>
    <div>415-555-0142</div>
    <div>elena.marsh@northharbor.us</div>
    <div>www.northharbor.us</div>
    <div class="gap"></div>
    <div>218 Laurel Ave, #4</div>
    <div>Oakland, CA 94610</div>
  </div>
  <svg class="bottom-swoop" viewBox="0 0 170 4" height="4" preserveAspectRatio="none"><path d="M0 4 Q85 -2 170 4 Z" fill="#262626"/></svg>
</section>

<!-- Business card, back -->
<section class="piece dark card-back">
  <div class="wordmark"><span class="mark-square"></span>North Harbor</div>
  <div class="site">www.<b>northharbor</b>.com</div>
</section>

<!-- Envelope, front -->
<section class="piece paper envelope-front">
  <div class="wordmark"><span class="mark-square"></span>North Harbor</div>
  <div class="return-address">
    <svg viewBox="0 0 24 24"><path d="M12 2a7 7 0 0 0-7 7c0 5 7 13 7 13s7-8 7-13a7 7 0 0 0-7-7zm0 9.5A2.5 2.5 0 1 1 12 6.5a2.5 2.5 0 0 1 0 5z" fill="#262626"/></svg>
    <span>218 Laurel Ave, #4<br>Oakland, CA 94610</span>
  </div>
  <svg class="bottom-swoop" viewBox="0 0 415 9" height="9" preserveAspectRatio="none"><path d="M0 9 Q207 -5 415 9 Z" fill="#262626"/></svg>
</section>

<!-- Envelope, back -->
<section class="piece paper envelope-back">
  <svg class="flap" viewBox="0 0 415 59" preserveAspectRatio="none"><path d="M0 0 H415 L403 52 Q402 59 395 59 H20 Q13 59 12 52 Z" fill="#262626"/></svg>
  <div class="mark-square-lg"></div>
  <div class="site">www.<b>northharbor</b>.us</div>
</section>

</body>
</html>
```